Web Design Project: Executive Coach

PLEASE check out http://tovrenly.com.sg/x/PixelHive/PixelHive_Brief/Blank.html

It is a better description of what I am after. It includes everything in this brief and in an easier format. (And...I don't have your design skills, so it doesn't look great.)

========

What the site offers
-
I am about to launch a one-person company that provides three services:
1) executive coaching
2) leadership training
3) psychotherapy to adults

My Unique Selling Point
-
My unique selling point is that I am a coach who is also a relatively senior psychologist. However, psychologists can be seen as scary and that may put people off.

The Biggest Challenge: The Target Audience
-
One challenge is that because I sell 3 services, I want to appeal to more than one demographic. They are:

1) The representative from HR of a company who wants to buy a leadership course or find a coach for an executive in the company. (Usually mid-40’s and older.)

2) The executives who will take the selection made by the head of HR and may choose me from 3 or 4 other options. (Usually late 30’s to mid 40’s. Both men and women. From multinational companies.)

3) Psychotherapy clients who are coming to be directly, not via HR, and who don’t want to feel insecure that they aren’t executives but still may be a good fit to work with me. (More women than men. Age 34-45. Typically have some European or American exposure.)

The Problem
-
The executives I see may or may not have some psychological concerns, but most will quite like that I am a psychologist as long as I’m not “scary” but “kind”. (Kind is key.) So while it is important to show I am a therapist, I don't want it to make executives embarrassed when a colleague says “Oh, I looked at this guy’s website. You aren't in therapy are you?”

As mentioned above, please check out the following link: http://tovrenly.com.sg/x/PixelHive/PixelHive_Brief/Blank.html

________
Please note, I originally posted this as 584207 Executive Coaching, Leadership Training, and Psychotherapy Website. With the help of one designer and also PixelHive customer support, I realized that I had requested only the design of a website, not the coding. I had offered the maximum amount, US$1000 (refundable). I am resubmitting the project here and I have guaranteed the funds. I am lowering the payment as I am now aware that I was only asking for design. I apologize for any inconvenience. And thank your for being interested in this project.
Updates

Project Deadline Extended
Reason: I would love to get started on the coding next week. So I hope to get your proposals in the next 3 days.

Target Market(s)

Primary audience: 34-44 year old men and women with some European / North American exposure

Industry/Entity Type

Leadership

Requirements
Must have
• Video on home page
Nice to have
• I would like have quotes slide in to a couple of the pages. These may have a photo of the author attached.

I would like Workvine integration with my business's Workvine page. (I haven't made one yet, so I'm not sure how it works.)

```html
<!DOCTYPE html>
<html lang="en">
<head>
<meta charset="utf-8">
<title>Halvorsen Consulting</title>
<link href="https://fonts.googleapis.com/css2?family=Cormorant+Garamond:wght@500&family=Source+Serif+4:wght@300&family=PT+Sans&family=Source+Sans+3:wght@300;400&display=swap" rel="stylesheet">
<style>
:root{
  --ink:#333;
  --text:#5a5a5a;
  --muted:#777;
  --nav-band:#e6e6e6;
  --stage:#e4e4e4;
  --tan:#cdc7a3;
  --panel:#2b2a26;
  --card-line:#e2e2e2;
  --white:#fff;
}
*{box-sizing:border-box;margin:0;padding:0}
html,body{width:963px;height:1200px;overflow:hidden;background:var(--white)}
body{position:relative;font-family:"Source Sans 3",sans-serif;color:var(--ink)}
.abs{position:absolute}
.site-header{left:0;top:0;width:963px;height:92px;background:linear-gradient(#fff,#f1f1f1)}
.brand{left:107px;top:34px;font-family:"Cormorant Garamond",serif;font-weight:500;font-size:25px;letter-spacing:.5px;text-transform:uppercase;color:#3a3a3a}
.main-nav{left:0;top:92px;width:963px;height:51px;background:linear-gradient(#efefef,#dcdcdc);border-top:1px solid #d6d6d6}
.main-nav ul{list-style:none;display:flex;position:absolute;left:87px;top:10px}
.main-nav li{font-family:"PT Sans",sans-serif;font-size:14px;color:#555;padding:5px 8px;margin-right:21px;height:26px}
.main-nav li.active{background:#fff;border-radius:2px;color:#444;box-shadow:0 0 3px rgba(0,0,0,.08)}
.stage{left:0;top:143px;width:963px;height:407px;background:var(--stage)}
.stage-shadow{left:130px;top:548px;width:703px;height:10px;border-radius:50%;box-shadow:0 4px 8px rgba(0,0,0,.12)}
.hero{left:96px;top:162px;width:774px;height:331px;background:var(--tan);border-radius:3px;overflow:hidden}
.hero-portrait{right:0;top:0;width:260px;height:331px;background:linear-gradient(90deg,var(--tan),#b8b194 35%,#8a8478 70%,#5f5b54)}
.hero-panel{left:69px;top:68px;width:414px;height:194px;background:var(--panel);border-radius:3px;color:#f2f2ee;font-family:"Source Serif 4",serif;font-weight:300}
.hero-name{position:absolute;left:35px;top:34px;font-size:22px}
.hero-role{position:absolute;left:34px;top:72px;width:360px;font-size:17.5px;line-height:26px;color:#e6e5df}
.btn-more{position:absolute;left:33px;top:140px;width:75px;height:28px;background:#1d1c19;border:1px solid #444;border-radius:3px;font-family:"Source Sans 3",sans-serif;font-size:14px;color:#eee;padding:5px 0 0 14px}
.arrow{top:150px}
.dots{left:452px;top:519px;display:flex;gap:5px}
.dots span{width:11px;height:11px;border-radius:50%;background:#fafafa;box-shadow:inset 0 1px 2px rgba(0,0,0,.15)}
.dots span.on{background:#bcbcbc;width:9px;height:11px}
.card{top:571px;width:254px;height:268px;border:1px solid var(--card-line);border-radius:3px;background:#fff;box-shadow:0 2px 4px rgba(0,0,0,.04)}
.card h2{height:42px;background:linear-gradient(#fff,#efefef);font-family:"PT Sans",sans-serif;font-weight:400;font-size:19px;color:#444;padding:9px 0 0 19px}
.card-photo{position:absolute;left:14px;top:50px;width:226px;height:137px}
.card h3{position:absolute;left:17px;top:196px;font-family:"PT Sans",sans-serif;font-weight:400;font-size:13px;color:#333}
.card p{position:absolute;left:17px;top:215px;width:192px;font-size:10.5px;line-height:15px;color:var(--text);font-weight:300}
.about h2{position:absolute;left:96px;top:870px;font-family:"PT Sans",sans-serif;font-weight:400;font-size:20px;color:#444}
.about p{position:absolute;left:96px;width:506px;font-size:10.5px;line-height:17.6px;color:var(--text);font-weight:300;text-align:justify}
.video{left:624px;top:884px;width:255px;height:174px;background:#d0d0d0;padding:5px}
.video-frame{width:245px;height:164px;background:linear-gradient(180deg,#6e6c66,#5a5853);position:relative}
.video-frame svg{position:absolute;left:101px;top:60px}
.site-footer{left:0;top:1087px;width:963px;height:113px;background:linear-gradient(#f2f2f2,#fff 40%)}
.footer-nav{position:absolute;left:83px;top:30px;font-family:"PT Sans",sans-serif;font-size:12px;color:#222}
.footer-nav span{margin:0 4px;color:#555}
.legal{position:absolute;left:83px;top:57px;font-size:10.5px;color:#666;font-weight:300}
.social{position:absolute;right:78px;top:29px;display:flex;gap:10px;font-family:"PT Sans",sans-serif;font-size:11px;color:#555}
.social li{list-style:none;display:flex;align-items:center;gap:4px}
.social li::before{content:"";width:9px;height:9px;border-radius:50%;background:#777}
</style>
</head>
<body>
<header class="site-header abs"><div class="brand abs">Halvorsen Consulting</div></header>
<nav class="main-nav abs"><ul>
  <li class="active">Welcome</li><li>Coaching</li><li>Training</li><li>Psychotherapy</li><li>FAQ</li><li>Publications</li><li>Clients</li><li>Resume</li><li>Contact</li>
</ul></nav>
<div class="stage abs"></div>
<div class="stage-shadow abs"></div>
<section class="hero abs">
  <div class="hero-portrait abs" role="img" aria-label="Portrait photo of the coach in a grey jacket and white shirt"></div>
  <div class="hero-panel abs">
    <div class="hero-name">Dr. Adrian Halvorsen</div>
    <div class="hero-role">Executive Coach, Leadership Trainer, Asst. Professor of Leadership Studies, Psychologist</div>
    <div class="btn-more">More &gt;&gt;</div>
  </div>
  <svg class="arrow abs" style="left:12px" width="14" height="26" viewBox="0 0 14 26"><path d="M12 2 2 13l10 11" fill="none" stroke="#fff" stroke-width="3"/></svg>
  <svg class="arrow abs" style="left:746px;top:156px" width="14" height="26" viewBox="0 0 14 26"><path d="M2 2l10 11L2 24" fill="none" stroke="#fff" stroke-width="3"/></svg>
</section>
<div class="dots abs"><span></span><span></span><span></span><span class="on"></span></div>

<article class="card abs" style="left:84px">
  <h2>Executive Coaching</h2>
  <div class="card-photo" role="img" aria-label="Photo of colleagues meeting around a laptop" style="background:linear-gradient(135deg,#f4f4f4,#c9b9a8 45%,#6d5f55 75%,#e8e8ec)"></div>
  <h3>Heading</h3><p>Fusce ultricies, orci ac feugiat suscipit, leo massa sodales velit, et scelerisque</p>
</article>
<article class="card abs" style="left:355px">
  <h2>Leadership Training</h2>
  <div class="card-photo" role="img" aria-label="Photo of a seated group in a training session, one man raising his hand" style="background:linear-gradient(135deg,#dfe3e8,#a9b3bd 40%,#2f3338 65%,#cfd6dd)"></div>
  <h3>Heading</h3><p>Fusce ultricies, orci ac feugiat suscipit, leo massa sodales velit, et scelerisque</p>
</article>
<article class="card abs" style="left:626px">
  <h2>Psychotherapy</h2>
  <div class="card-photo" role="img" aria-label="Photo of a woman in a red top sitting calmly on a sofa" style="background:linear-gradient(135deg,#eef0f1,#d8d4d0 40%,#c2303c 55%,#e9e5e2 75%)"></div>
  <h3>Heading</h3><p>Fusce ultricies, orci ac feugiat suscipit, leo massa sodales velit, et scelerisque</p>
</article>

<section class="about">
  <h2>About Dr. Adrian Halvorsen</h2>
  <p style="top:907px">Our clients include highly accomplished individuals who seek to push their performance further and people who may not be well and who hope to overcome significant obstacles. With organizations, he conducts training in leadership and management.</p>
  <p style="top:970px">He is Assistant Professor of Leadership Studies at the Tan Wei Ling School of Public Policy (the top ranked public policy school in Asia) which is located in the Meridian University of Singapore (25th in World University Rankings). Dr. Halvorsen works with policy makers from more than 50 countries. His doctorate in psychology was from Westbrook University and his postdoctoral training was at Kestrel University where he held specific responsibilities for working with Kestrel Business School faculty, staff, and students.</p>
</section>
<div class="video abs">
  <div class="video-frame" role="img" aria-label="Video still of the coach speaking to camera">
    <svg width="42" height="42" viewBox="0 0 42 42"><circle cx="21" cy="21" r="21" fill="#fff" fill-opacity=".3"/><path d="M17 13v16l12-8z" fill="#111"/></svg>
  </div>
</div>

<footer class="site-footer abs">
  <div class="footer-nav">Home<span>|</span>Coaching<span>|</span>Training<span>|</span>Psychotherapy<span>|</span>FAQ<span>|</span>Publications<span>|</span>Clients<span>|</span>Resume<span>|</span>Contact</div>
  <div class="legal">© 2013 Company Name.&nbsp; All right reserved.&nbsp; Term of Use</div>
  <ul class="social"><li>Friendly</li><li>Workvine</li><li>Chirpline</li></ul>
</footer>
</body>
</html>
```